Banners Ads for Marketing Company

We are looking to have banner ads designed that will carry a common theme to be used across the following sizes (all these sizes will need to be created): 468 x 60, 728 x 90, 250 x 250, 300 x 250, 120 x 600, 160 x 600.

We are a leading SEO firm. We are often featured in Varnell, Startwright, The Bramblecote Ledger, Query Index Lookout, Query Index Gazette, etc for our SEO expertise. We have hundreds of clients and we are recognized by Rankvale.com, Finestlistingfirms.com, Listingagencyratings.com, and Outreachsphere.com as one of the top SEO firms in the U.S.

The goal of our campaign is to get business professional to click on these ads to get more information about who we are and request a quote. We will be using these ads for retargeting campaigns as well as regular display campaigns. The banners need to be clean and crisp and get people into our sales funnel.

Our website is: http://www.brightcorvale.example/

```html
<!DOCTYPE html>
<html lang="en">
<head>
<meta charset="utf-8">
<title>Brightcorvale Banner Set</title>
<link rel="stylesheet" href="https://fonts.googleapis.com/css2?family=Arimo:wght@400;700&display=swap">
<style>
  :root {
    --page: #ffffff;
    --navy: #0d1a33;
    --navy-glow: #2a3d63;
    --gold-light: #f5e3ab;
    --gold: #e4c274;
    --gold-deep: #cfa652;
    --gold-shadow: #9c7a3a;
    --arc-light: #ffd27a;
    --arc: #e39a22;
    --ink-brown: #7a5832;
    --star: #b58a55;
    --btn-light: #ffab2e;
    --btn: #f27a00;
    --btn-edge: #d96a00;
    --btn-ink: #5a2e0c;
    --btn-dot: #4a2a12;
    --base-red: #a8403a;
    --label: #1a1a1a;
    --logo-ink: #ffffff;
    --logo-dot: #f0a81e;
  }
  * { box-sizing: border-box; margin: 0; padding: 0; }
  html, body { width: 1200px; height: 1200px; overflow: hidden; background: var(--page); }
  body { font-family: "Arimo", Arial, sans-serif; }

  .board { position: absolute; left: 0; top: 0; width: 860px; height: 860px; transform: scale(1.3953); transform-origin: 0 0; }

  .banner { position: absolute; overflow: hidden; background: var(--navy); }
  .banner--leaderboard { left: 75px; top: 32px; width: 728px; height: 90px; }
  .banner--rectangle { left: 75px; top: 194px; width: 300px; height: 250px; border: 1px solid #c9c9c9; }
  .banner--skyscraper { left: 643px; top: 194px; width: 160px; height: 600px; border: 1px solid #c9c9c9; }
  .banner__shapes { position: absolute; inset: 0; width: 100%; height: 100%; }

  .size-label { position: absolute; font-size: 15px; color: var(--label); transform: translateX(-50%); }

  .brand { position: absolute; display: flex; align-items: center; gap: 5px; color: var(--logo-ink); font-size: 14px; font-weight: 400; white-space: nowrap; }
  .brand__dot { width: 10px; height: 10px; border-radius: 50%; background: var(--logo-dot); flex: none; }

  .bulb { position: absolute; border-radius: 50%;
    background: radial-gradient(circle at 50% 42%, #ffffff 0%, #dfe3ea 28%, #8f98a8 48%, rgba(42,61,99,0.5) 66%, rgba(13,26,51,0) 78%); }

  .headline { position: absolute; color: var(--ink-brown); font-weight: 700; line-height: 1; }
  .headline__title { font-size: 28px; display: block; }
  .headline__sub { font-size: 17px; display: block; }

  .star { position: absolute; width: 24px; height: 24px; }

  .cta { position: absolute; display: flex; align-items: center; justify-content: space-between; padding: 0 4px 0 14px;
    border: 1px solid var(--btn-edge); border-radius: 4px;
    background: linear-gradient(180deg, var(--btn-light) 0%, var(--btn) 100%);
    box-shadow: 0 2px 3px rgba(0,0,0,0.3);
    color: var(--btn-ink); font-size: 16px; font-weight: 700; }
  .cta__arrow { width: 30px; height: 30px; border-radius: 50%; background: var(--btn-dot); display: flex; align-items: center; justify-content: center; }
  .cta__arrow svg { width: 14px; height: 14px; }
</style>
</head>
<body>
<div class="board">

  <!-- 728 x 90 -->
  <div class="banner banner--leaderboard">
    <svg class="banner__shapes" viewBox="0 0 728 90" preserveAspectRatio="none">
      <defs>
        <linearGradient id="lb-ribbon" x1="0" x2="1" y1="0" y2="0">
          <stop offset="0" stop-color="#e9cf86"/><stop offset="0.4" stop-color="#f6e6b2"/><stop offset="1" stop-color="#e2c070"/>
        </linearGradient>
        <linearGradient id="lb-arc" x1="0" x2="1"><stop offset="0" stop-color="#c9760f"/><stop offset="0.5" stop-color="#ffd27a"/><stop offset="1" stop-color="#e39a22"/></linearGradient>
      </defs>
      <rect width="728" height="90" fill="var(--navy)"/>
      <rect x="222" y="68" width="506" height="15" fill="#ffffff"/>
      <rect y="83" width="728" height="7" fill="var(--base-red)"/>
      <path d="M205,0 Q236,45 212,90 L226,90 Q250,45 219,0 Z" fill="url(#lb-arc)"/>
      <polygon points="500,16 580,16 556,49 580,82 510,82" fill="var(--gold-deep)"/>
      <polygon points="505,71 522,71 522,82" fill="var(--gold-shadow)"/>
      <rect x="222" y="6" width="283" height="65" fill="url(#lb-ribbon)"/>
    </svg>
    <div class="brand" style="left:6px; top:36px;"><span class="brand__dot"></span>brightcorvale.example</div>
    <div class="bulb" role="img" aria-label="Glowing light bulb illustration" style="left:160px; top:2px; width:70px; height:86px;"></div>
    <div class="headline" style="left:238px; top:12px;">
      <span class="headline__title">Need Visibility?</span>
      <span class="headline__sub" style="margin-top:3px;">We Are Your Marketing Firm</span>
    </div>
    <svg class="star" viewBox="0 0 24 24" style="left:497px; top:25px;"><polygon points="12,1 15,9 23,9 16.5,14 19,22 12,17 5,22 7.5,14 1,9 9,9" fill="var(--star)"/></svg>
    <div class="cta" style="left:582px; top:26px; width:134px; height:40px;">Click Here<span class="cta__arrow"><svg viewBox="0 0 14 14"><path d="M5 2 L10 7 L5 12" fill="none" stroke="#fff" stroke-width="2.4"/></svg></span></div>
  </div>
  <div class="size-label" style="left:440px; top:129px;">728X90</div>

  <!-- 300 x 250 -->
  <div class="banner banner--rectangle">
    <svg class="banner__shapes" viewBox="0 0 300 250" preserveAspectRatio="none">
      <defs>
        <radialGradient id="rc-ribbon" cx="0.25" cy="0.45" r="0.8">
          <stop offset="0" stop-color="#f8ecc4"/><stop offset="1" stop-color="#e2c070"/>
        </radialGradient>
        <linearGradient id="rc-arc" x1="0" x2="1"><stop offset="0" stop-color="#e39a22"/><stop offset="0.5" stop-color="#ffd98a"/><stop offset="1" stop-color="#d98a18"/></linearGradient>
      </defs>
      <rect width="300" height="250" fill="#ffffff"/>
      <rect width="300" height="145" fill="var(--navy)"/>
      <rect y="242" width="300" height="8" fill="var(--base-red)"/>
      <path d="M0,58 Q150,48 300,62 L300,80 Q150,66 0,76 Z" fill="url(#rc-arc)"/>
      <polygon points="238,80 266,80 300,140 300,203 238,203" fill="var(--gold-deep)"/>
      <polygon points="238,189 258,189 258,203" fill="var(--gold-shadow)"/>
      <rect x="0" y="74" width="240" height="115" fill="url(#rc-ribbon)"/>
    </svg>
    <div class="brand" style="left:20px; top:18px;"><span class="brand__dot"></span>brightcorvale.example</div>
    <div class="bulb" role="img" aria-label="Glowing light bulb illustration" style="left:196px; top:-4px; width:56px; height:68px;"></div>
    <div class="headline" style="left:9px; top:104px;">
      <span class="headline__title" style="font-size:26px;">Need Visibility?</span>
      <span class="headline__sub" style="margin-top:2px; line-height:1.1;">We Are Your<br>Marketing Firm</span>
    </div>
    <svg class="star" viewBox="0 0 24 24" style="left:210px; top:118px;"><polygon points="12,1 15,9 23,9 16.5,14 19,22 12,17 5,22 7.5,14 1,9 9,9" fill="var(--star)"/></svg>
    <div class="cta" style="left:77px; top:195px; width:136px; height:43px;">Click Here<span class="cta__arrow"><svg viewBox="0 0 14 14"><path d="M5 2 L10 7 L5 12" fill="none" stroke="#fff" stroke-width="2.4"/></svg></span></div>
  </div>
  <div class="size-label" style="left:219px; top:451px;">300X250</div>

  <!-- 160 x 600 -->
  <div class="banner banner--skyscraper">
    <svg class="banner__shapes" viewBox="0 0 160 600" preserveAspectRatio="none">
      <defs>
        <radialGradient id="sk-ribbon" cx="0.5" cy="0.4" r="0.8">
          <stop offset="0" stop-color="#f8ecc4"/><stop offset="1" stop-color="#e2c070"/>
        </radialGradient>
        <linearGradient id="sk-arc" x1="0" x2="1"><stop offset="0" stop-color="#e39a22"/><stop offset="0.5" stop-color="#ffd98a"/><stop offset="1" stop-color="#d98a18"/></linearGradient>
      </defs>
      <rect width="160" height="600" fill="#ffffff"/>
      <rect width="160" height="360" fill="var(--navy)"/>
      <rect y="587" width="160" height="13" fill="var(--base-red)"/>
      <path d="M0,176 Q80,160 160,176 L160,192 Q80,178 0,192 Z" fill="url(#sk-arc)"/>
      <polygon points="7,403 147,403 147,513 77,471 7,513" fill="var(--gold)"/>
      <rect x="14" y="189" width="141" height="242" fill="url(#sk-ribbon)"/>
    </svg>
    <div class="brand" style="left:8px; top:30px; font-size:12px;"><span class="brand__dot"></span>brightcorvale.example</div>
    <div class="bulb" role="img" aria-label="Glowing light bulb illustration" style="left:30px; top:62px; width:100px; height:116px;"></div>
    <div class="headline" style="left:14px; top:214px; width:141px; text-align:center;">
      <span class="headline__title" style="font-size:26px; line-height:1.15;">Need<br>Visibility?</span>
      <span class="headline__sub" style="margin-top:6px; line-height:1.27;">We<br>Are<br>Your<br>Marketing<br>Firm</span>
    </div>
    <svg class="star" viewBox="0 0 24 24" style="left:67px; top:394px;"><polygon points="12,1 15,9 23,9 16.5,14 19,22 12,17 5,22 7.5,14 1,9 9,9" fill="var(--star)"/></svg>
    <div class="cta" style="left:12px; top:528px; width:135px; height:43px;">Click Here<span class="cta__arrow"><svg viewBox="0 0 14 14"><path d="M5 2 L10 7 L5 12" fill="none" stroke="#fff" stroke-width="2.4"/></svg></span></div>
  </div>
  <div class="size-label" style="left:722px; top:803px;">160X600</div>

</div>
</body>
</html>
```